Nail salon window signage design

We need new signage to be designed for our existing nail salon. The sign will be a large sticker that will stick onto the glass window at the front.

Some of the services we provide are:
Manicures
Pedicures
Velora Gel Builder
Acrylic Nails
KVT
Brenlux
Gel Polish
You may wish to have our services listed on the sign but is not compulsory.

I have also attached our logo which can be used on the sign but is not compulsory.

I have also attached a photo of the front of our salon and the sign will be where I have outlined in yellow.

The size of the sign will be 119cm wide and 170cm high.

I am open to any nice classy design you can think of.

```html
<!DOCTYPE html>
<html lang="en">
<head>
<meta charset="utf-8">
<title>Aurelle Nails – Window Sign</title>
<link rel="stylesheet" href="https://fonts.googleapis.com/css2?family=Bodoni+Moda:opsz,wght@6..96,400&display=swap">
<style>
  :root {
    --paper: #ffffff;
    --gold: #d1af78;
    --wine: #8b1a2b;
  }
  * { margin: 0; padding: 0; box-sizing: border-box; }
  html, body {
    width: 1200px;
    height: 1200px;
    overflow: hidden;
    background: var(--paper);
  }
  .sign {
    position: relative;
    width: 1200px;
    height: 1200px;
    background: var(--paper);
    font-family: "Bodoni Moda", "Didot", serif;
  }
  .frame {
    position: absolute;
    inset: 0;
    width: 1200px;
    height: 1200px;
  }
  .ornament {
    position: absolute;
    border-radius: 50%;
    background: radial-gradient(ellipse at center, rgba(209,175,120,0.55) 0%, rgba(209,175,120,0.18) 55%, rgba(209,175,120,0) 75%);
  }
  .ornament--top { left: 500px; top: 116px; width: 237px; height: 86px; }
  .ornament--bottom { left: 495px; top: 1004px; width: 236px; height: 86px; }
  .brand {
    position: absolute;
    left: 0;
    width: 1200px;
    top: 318px;
    text-align: center;
    color: var(--wine);
    font-size: 56px;
    font-weight: 400;
    letter-spacing: 0.02em;
    line-height: 1;
  }
  .services {
    position: absolute;
    left: 0;
    width: 1212px;
    top: 500px;
    list-style: none;
    text-align: center;
    color: var(--gold);
    font-size: 42px;
    font-weight: 400;
    letter-spacing: 0.07em;
    line-height: 54.9px;
  }
</style>
</head>
<body>
<main class="sign">
  <svg class="frame" viewBox="0 0 1200 1200" aria-hidden="true">
    <g fill="none" stroke="var(--gold)" stroke-width="3">
      <polyline points="445,180.5 287.5,180.5 287.5,1021.5 441,1021.5"/>
      <polyline points="770,180.5 935.5,180.5 935.5,1021.5 770,1021.5"/>
    </g>
  </svg>
  <div class="ornament ornament--top" role="img" aria-label="Gold scrollwork flourish with a diamond at its centre"></div>
  <div class="ornament ornament--bottom" role="img" aria-label="Gold scrollwork flourish with a diamond at its centre"></div>

  <h1 class="brand">Aurelle Nails</h1>

  <ul class="services">
    <li>Manicures</li>
    <li>Pedicures</li>
    <li>Velora Gel Builder</li>
    <li>Acrylic Nails</li>
    <li>KVT</li>
    <li>Brenlux</li>
    <li>Gel Polish</li>
  </ul>
</main>
</body>
</html>
```